Looking to develop game card. It will be included in Dozen Golf Balls Using the DaxPROTLE THEME ( 6 new games) and (6 old games) Attached is a picture of a three fold score card. Six games on the front layout and six on the back. Sample is "name of game and rules" Be creative in the set up. should be easy to read and simple to follow.

```html
<!DOCTYPE html>
<html lang="en">
<head>
<meta charset="utf-8">
<title>DaxPROTLE Game Score Card</title>
<link href="https://fonts.googleapis.com/css2?family=Barlow+Condensed:ital,wght@0,600;0,700;0,800;1,700;1,800&family=Arimo:ital,wght@0,400;0,700;1,400&family=Playfair+Display:ital,wght@1,600&display=swap" rel="stylesheet">
<style>
:root{
  --bg:#1ea4f0;
  --paper:#ffffff;
  --ink:#1b1b1b;
  --green:#1f4d2b;
  --green-mid:#2f7a3a;
  --navy:#1b3a70;
  --red:#c4161c;
  --blue:#1e4fa8;
  --orange:#e8641b;
  --purple:#6a2ca0;
  --gold:#c98a12;
  --yellow:#f7d51d;
  --rule:#d9d9d9;
  --row-red:#f9cccc;
  --row-blue:#c9def6;
  --row-green:#d2ecc9;
  --row-orange:#fbd4b6;
  --row-purple:#ded2f1;
  --row-yellow:#f8e2ad;
  --row-gray:#e2e2e2;
}
*{box-sizing:border-box;margin:0;padding:0}
html,body{width:1200px;height:800px;overflow:hidden;background:var(--bg)}
body{position:relative;font-family:"Arimo",sans-serif;color:var(--ink)}
.panel{position:absolute;background:var(--paper);overflow:hidden}
.p-rules-top{left:23px;top:8px;width:391px;height:383px}
.p-score-top{left:418px;top:8px;width:377px;height:383px}
.p-cover-top{left:798px;top:8px;width:383px;height:383px}
.p-rules-bot{left:23px;top:405px;width:391px;height:385px}
.p-score-bot{left:418px;top:405px;width:377px;height:385px}
.p-cover-bot{left:798px;top:405px;width:383px;height:385px}

/* rules panel */
.rules-head{height:48px;display:flex;align-items:center;padding-left:34px;gap:8px;color:#fff}
.rules-head.new{background:var(--green)}
.rules-head.classic{background:var(--navy)}
.rules-head .big{font-family:"Barlow Condensed",sans-serif;font-weight:800;font-style:italic;font-size:44px;color:var(--yellow);line-height:1}
.rules-head h2{font-family:"Barlow Condensed",sans-serif;font-weight:800;font-style:italic;font-size:26px;line-height:1;letter-spacing:.3px}
.rules-head h2 .accent{color:var(--yellow)}
.rules-head p{font-family:"Barlow Condensed",sans-serif;font-weight:700;font-size:11px;letter-spacing:.4px;text-align:center}
.rule{position:relative;height:111px;padding:8px 92px 0 60px;border-bottom:1px solid var(--rule)}
.rule:last-child{border-bottom:0}
.rule .num{position:absolute;left:10px;top:10px;width:38px;height:38px;border-radius:50%;background:var(--accent);color:#fff;font-family:"Barlow Condensed",sans-serif;font-weight:800;font-size:28px;display:flex;align-items:center;justify-content:center}
.rule h3{font-family:"Barlow Condensed",sans-serif;font-weight:800;font-style:italic;font-size:19px;color:var(--accent);line-height:1.05}
.rule h3 sup{font-size:8px}
.rule .tag{font-style:italic;font-size:10px;margin:1px 0 5px}
.rule ol{list-style:none;font-size:7.6px;line-height:1.45}
.rule ol li{display:flex;gap:4px}
.rule ol li b{flex:none;width:9px;height:9px;border-radius:50%;background:var(--accent);color:#fff;font-size:6px;display:flex;align-items:center;justify-content:center;margin-top:1px}
.rule .after{font-size:7.6px;line-height:1.45;margin-top:2px}
.rule .art{position:absolute;right:10px;top:12px;width:78px;height:86px;border-radius:8px;background:linear-gradient(#eef2ee,#9fc98f)}
.red{--accent:var(--red)} .blue{--accent:var(--blue)} .green{--accent:var(--green-mid)}
.orange{--accent:var(--orange)} .purple{--accent:var(--purple)} .gold{--accent:var(--gold)}

/* score panel */
.p-score-top,.p-score-bot{padding:8px 8px 0 9px}
.sc-title{display:flex;justify-content:space-between;align-items:baseline;margin:2px 0 5px}
.sc-title h4{font-family:"Barlow Condensed",sans-serif;font-weight:700;font-size:15px;color:var(--ink)}
.sc-title span{font-family:"Barlow Condensed",sans-serif;font-weight:700;font-size:8.5px;letter-spacing:.3px}
.sc-title.navy h4,.sc-title.navy span{color:var(--navy)}
table.card{width:100%;border-collapse:collapse;table-layout:fixed;margin-bottom:8px}
table.card th{height:17px;color:#fff;font-size:9px;font-weight:700;border:1px solid #fff}
table.card.g th{background:var(--green)} table.card.n th{background:var(--navy)}
table.card th.lbl{width:80px}
table.card td{height:29px;border:1px solid #9aa59a}
table.card td.game{font-family:"Barlow Condensed",sans-serif;text-align:center;line-height:1.05;font-size:11.5px;font-weight:700}
table.card td.game small{display:block;font-family:"Arimo",sans-serif;font-size:7.5px}
.gr{background:var(--row-red);color:var(--red)} .gb{background:var(--row-blue);color:var(--blue)}
.gg{background:var(--row-green);color:var(--green)} .go{background:var(--row-orange);color:var(--orange)}
.gp{background:var(--row-purple);color:var(--purple)} .gy{background:var(--row-yellow);color:#9a5d00}
.gx{background:var(--row-gray);color:var(--ink)}
.boxes{display:flex;gap:9px;margin-top:2px}
.box{flex:1;border:1px solid #9aa;border-radius:5px;height:93px;padding:4px 6px}
.box h5{font-family:"Barlow Condensed",sans-serif;font-weight:700;font-size:11px;margin-bottom:2px}
.box .line{height:18px;border-bottom:1px solid #c8c8c8;font-size:9px;display:flex;align-items:flex-end;padding-bottom:1px}

/* covers */
.photo{position:absolute;inset:0}
.photo.coast{background:linear-gradient(180deg,#3c8fe0 0%,#8cc7f0 36%,#5f7f9e 45%,#1d5b93 52%,#3f7a3a 64%,#7fb84b 82%,#4e8a2e 100%)}
.photo.bay{background:linear-gradient(180deg,#1f77d6 0%,#6fb6ee 45%,#9fc8e0 58%,#3a7aa8 66%,#4b8b3a 76%,#7cb84c 100%)}
.photo.bag{left:auto;right:0;top:20px;width:105px;bottom:0;background:linear-gradient(90deg,#3b4a5a,#e9ecef 55%,#f7f7f7)}
.cover-text{position:absolute;color:#fff;text-align:center}
.course-name{top:36px;left:58px;font-family:"Playfair Display",serif;font-style:italic;font-weight:600;font-size:32px;line-height:1.05;text-align:left}
.course-name span{display:block}
.course-name .l2{padding-left:0}
.course-name .l3{padding-left:105px}
.mark{position:absolute;top:18px;left:238px;width:36px;height:36px;border-radius:50%;background:#fff}
.sc-label{top:132px;left:0;right:0;color:var(--navy);font-family:"Barlow Condensed",sans-serif;font-weight:700}
.sc-label .a{font-size:14px;letter-spacing:2.5px;padding-left:105px}
.sc-label .b{font-size:11px;letter-spacing:.6px;padding-left:105px;margin-top:1px}
.cover-foot{bottom:8px;left:0;right:0;font-family:"Barlow Condensed",sans-serif;font-weight:700;line-height:1.05}
.cover-foot .brand{font-size:24px;font-weight:800}
.cover-foot .sub{font-size:13px;letter-spacing:1px}
.cover-foot .tag{font-size:10px;letter-spacing:.2px;margin-top:2px}
.hero{top:22px;left:28px;width:250px;font-family:"Barlow Condensed",sans-serif}
.hero .brand{font-size:50px;font-weight:800;line-height:1;transform:rotate(-3deg)}
.hero .sub{font-size:21px;font-weight:700;transform:rotate(-3deg);margin-top:2px}
.hero hr{border:0;border-top:2px solid rgba(255,255,255,.85);width:110px;margin:16px auto 12px}
.hero .pitch{font-size:16px;font-weight:700;font-style:italic;line-height:1.2;transform:rotate(-3deg)}
.play{position:absolute;left:22px;bottom:14px;color:#fff;font-family:"Barlow Condensed",sans-serif;font-weight:700;font-size:16px;line-height:1.05}
.towel{position:absolute;right:10px;bottom:40px;width:70px;transform:rotate(-14deg);font-family:"Barlow Condensed",sans-serif;font-weight:700;font-style:italic;font-size:15px;color:#222;line-height:1.05;text-align:center}
</style>
</head>
<body>

<!-- front side: new games -->
<section class="panel p-rules-top">
  <header class="rules-head new">
    <span class="big">6</span>
    <div><h2><span class="accent">NEW</span> DAXPROTLE GAMES</h2><p>NEW CHALLENGES. SAME GREAT FUN.</p></div>
  </header>
  <article class="rule red">
    <div class="num">1</div>
    <h3>DAXPROTLE ROULETTE<sup>™</sup></h3>
    <p class="tag">Every hole. Everyone’s watching.</p>
    <ol>
      <li><b>1</b><span>Shuffle the 4 Ball Cards (Slice, Hook, Shank, DaxPROTLE).</span></li>
      <li><b>2</b><span>Each player draws one card at the first tee.<br>That card is YOUR DISASTER for the round.</span></li>
      <li><b>3</b><span>If you hit your disaster, pay 1 point or $1 to the pot.</span></li>
      <li><b>4</b><span>If someone else hits YOUR disaster, they pay YOU!</span></li>
    </ol>
    <div class="art" role="img" aria-label="Golf ball on grass with a red slash"></div>
  </article>
  <article class="rule blue">
    <div class="num">2</div>
    <h3>CALL YOUR DAXPROTLE<sup>™</sup></h3>
    <p class="tag">Think he can pull it off?</p>
    <ol>
      <li><b>1</b><span>Before the shot, a player calls out: “I’M CALLING DAXPROTLE!”</span></li>
      <li><b>2</b><span>If the shot ends up in deep trouble, the caller owes $1.</span></li>
      <li><b>3</b><span>If the shot is spectacular (or stays in play), the caller collects $1.</span></li>
      <li><b>4</b><span>If the golfer pulls off the shot, the caller owes HIM $1.</span></li>
    </ol>
    <div class="art" role="img" aria-label="Silhouette of a golfer mid-swing with a speech bubble"></div>
  </article>
  <article class="rule green">
    <div class="num">3</div>
    <h3>THE FOUR HORSEMEN<sup>™</sup></h3>
    <p class="tag">Every round has them. Collect them all.</p>
    <ol>
      <li><b>1</b><span>The Slicer – 1 point</span></li>
      <li><b>2</b><span>The Hook – 1 point</span></li>
      <li><b>3</b><span>The Shank Ball – 2 points</span></li>
      <li><b>4</b><span>The DaxPROTLE – 3 points</span></li>
    </ol>
    <p class="after">Add up your points at the end of 18 holes.<br>Lowest score wins.</p>
    <div class="art" role="img" aria-label="Silhouette of four riders on horseback holding golf clubs"></div>
  </article>
</section>

<section class="panel p-score-top">
  <div class="sc-title"><h4>FRONT 9 – GAMES 1–3</h4><span>PLAY IT. SCORE IT. DAXPROTLE IT.</span></div>
  <table class="card g">
    <tr><th class="lbl">HOLE</th><th>1</th><th>2</th><th>3</th><th>4</th><th>5</th><th>6</th><th>7</th><th>8</th><th>9</th><th>OUT</th></tr>
    <tr><td class="game gr">GAME 1<small>Roulette</small></td><td></td><td></td><td></td><td></td><td></td><td></td><td></td><td></td><td></td><td></td></tr>
    <tr><td class="game gb">GAME 2<small>Call Your DaxPROTLE</small></td><td></td><td></td><td></td><td></td><td></td><td></td><td></td><td></td><td></td><td></td></tr>
    <tr><td class="game gg">GAME 3<small>Four Horsemen</small></td><td></td><td></td><td></td><td></td><td></td><td></td><td></td><td></td><td></td><td></td></tr>
  </table>
  <div class="sc-title"><h4>BACK 9 – GAMES 4–6</h4></div>
  <table class="card g">
    <tr><th class="lbl">HOLE</th><th>10</th><th>11</th><th>12</th><th>13</th><th>14</th><th>15</th><th>16</th><th>17</th><th>18</th><th>IN</th><th>TOT</th></tr>
    <tr><td class="game go">GAME 4<small>Insurance</small></td><td></td><td></td><td></td><td></td><td></td><td></td><td></td><td></td><td></td><td></td><td></td></tr>
    <tr><td class="game gp">GAME 5<small>DaxPROTLE Ball</small></td><td></td><td></td><td></td><td></td><td></td><td></td><td></td><td></td><td></td><td></td><td></td></tr>
    <tr><td class="game gy">GAME 6<small>Bachelor’s Revenge</small></td><td></td><td></td><td></td><td></td><td></td><td></td><td></td><td></td><td></td><td></td><td></td></tr>
  </table>
  <div class="boxes">
    <div class="box"><h5>PLAYERS</h5><div class="line">1</div><div class="line">2</div><div class="line">3</div><div class="line">4</div></div>
    <div class="box"><h5>NOTES / SKINS / POT</h5><div class="line"></div><div class="line"></div><div class="line"></div><div class="line"></div></div>
  </div>
</section>

<section class="panel p-cover-top">
  <div class="photo coast" role="img" aria-label="Coastal golf course with ocean, mountains and green fairway"></div>
  <div class="mark"></div>
  <div class="cover-text course-name"><span>The</span><span class="l2">Harbor Ridge</span><span class="l3">Course</span></div>
  <div class="cover-text sc-label"><div class="a">SCORE CARD</div><div class="b">6 NEW GAMES • 6 CLASSIC GAMES</div></div>
  <div class="cover-text cover-foot"><div class="brand">DAXPROTLE™</div><div class="sub">DOZEN GOLF BALLS</div><div class="tag">MORE GAMES. MORE LAUGHS. A BETTER ROUND.</div></div>
</section>

<!-- back side: classic games -->
<section class="panel p-rules-bot">
  <header class="rules-head classic">
    <span class="big">6</span>
    <div><h2>CLASSIC DAXPROTLE GAMES</h2><p>THE ORIGINALS. STILL A CROWD FAVORITE.</p></div>
  </header>
  <article class="rule orange">
    <div class="num">4</div>
    <h3>DAXPROTLE INSURANCE<sup>™</sup></h3>
    <p class="tag">Because courage deserves a reward.</p>
    <ol>
      <li><b>1</b><span>Before your tee shot, say “INSURANCE” and put $1 in the pot.</span></li>
      <li><b>2</b><span>If your ball ends up in the woods, deep rough, or any true DaxPROTLE, the pot pays YOU $5.</span></li>
      <li><b>3</b><span>If you hit the fairway, your $1 stays in the pot.</span></li>
    </ol>
    <div class="art" role="img" aria-label="Golf ball on a shield emblem"></div>
  </article>
  <article class="rule purple">
    <div class="num">5</div>
    <h3>THE DAXPROTLE BALL<sup>™</sup></h3>
    <p class="tag">One ball to rule them all.</p>
    <ol>
      <li><b>1</b><span>The DaxPROTLE Ball starts with Player #1.</span></li>
      <li><b>2</b><span>If you make PAR or better, pass the ball to another player.</span></li>
      <li><b>3</b><span>Bogey or worse? You keep it.</span></li>
      <li><b>4</b><span>Lose the DaxPROTLE Ball and YOU BUY THE FIRST ROUND at the clubhouse.</span></li>
    </ol>
    <div class="art" role="img" aria-label="Golf ball in grass printed with the game name"></div>
  </article>
  <article class="rule gold">
    <div class="num">6</div>
    <h3>BACHELOR’S REVENGE<sup>™</sup></h3>
    <p class="tag">The groom gets one free pass.</p>
    <ol>
      <li><b>1</b><span>The groom gets ONE DAXPROTLE PARDON per nine holes.</span></li>
      <li><b>2</b><span>When he hits a truly awful shot, he can declare: “DAXPROTLE!”</span></li>
      <li><b>3</b><span>He gets a free replacement ball, BUT the other 3 players choose WHERE he has to play it from.</span></li>
    </ol>
    <div class="art" role="img" aria-label="Silhouette of a golfer putting beside pine trees"></div>
  </article>
</section>

<section class="panel p-score-bot">
  <div class="sc-title navy"><h4>FRONT 9 – GAMES 7–9</h4><span>SAME COURSE. DIFFERENT KIND OF TROUBLE.</span></div>
  <table class="card n">
    <tr><th class="lbl">HOLE</th><th>1</th><th>2</th><th>3</th><th>4</th><th>5</th><th>6</th><th>7</th><th>8</th><th>9</th><th>OUT</th></tr>
    <tr><td class="game gr">GAME 7<small>Wolf</small></td><td></td><td></td><td></td><td></td><td></td><td></td><td></td><td></td><td></td><td></td></tr>
    <tr><td class="game gb">GAME 8<small>Snake</small></td><td></td><td></td><td></td><td></td><td></td><td></td><td></td><td></td><td></td><td></td></tr>
    <tr><td class="game gg">GAME 9<small>Sixes</small></td><td></td><td></td><td></td><td></td><td></td><td></td><td></td><td></td><td></td><td></td></tr>
  </table>
  <div class="sc-title navy"><h4>BACK 9 – GAMES 10–12</h4></div>
  <table class="card n">
    <tr><th class="lbl">HOLE</th><th>10</th><th>11</th><th>12</th><th>13</th><th>14</th><th>15</th><th>16</th><th>17</th><th>18</th><th>IN</th><th>TOT</th></tr>
    <tr><td class="game gx">GAME 10<small>Skins</small></td><td></td><td></td><td></td><td></td><td></td><td></td><td></td><td></td><td></td><td></td><td></td></tr>
    <tr><td class="game gb">GAME 11<small>Vegas</small></td><td></td><td></td><td></td><td></td><td></td><td></td><td></td><td></td><td></td><td></td><td></td></tr>
    <tr><td class="game gg">GAME 12<small>Bingo-Bango-Bongo</small></td><td></td><td></td><td></td><td></td><td></td><td></td><td></td><td></td><td></td><td></td><td></td></tr>
  </table>
  <div class="boxes">
    <div class="box"><h5>PLAYERS</h5><div class="line">1</div><div class="line">2</div><div class="line">3</div><div class="line">4</div></div>
    <div class="box"><h5>NOTES / SKINS / POT</h5><div class="line"></div><div class="line"></div><div class="line"></div><div class="line"></div></div>
  </div>
</section>

<section class="panel p-cover-bot">
  <div class="photo bay" role="img" aria-label="Seaside golf course under a blue sky"></div>
  <div class="photo bag" role="img" aria-label="Golf bag with irons and a white towel"></div>
  <div class="cover-text hero">
    <div class="brand">DAXPROTLE™</div>
    <div class="sub">DOZEN GOLF BALLS</div>
    <hr>
    <div class="pitch">TWICE THE GAMES.<br>A DOZEN GOOD REASONS<br>TO PLAY TOGETHER.</div>
  </div>
  <div class="towel">BAD SHOTS BRING GOOD PEOPLE TOGETHER.</div>
  <div class="play">PLAY BOLD.<br>PLAY DAXPROTLE.™</div>
</section>

</body>
</html>
```